Brantley Studios photography and video creator

I need a business card for my production company. I shoot photography and videography for real estate, adventure sports and businesses

Contact Information for Business Card

simple not to busy

Colors

Designer to choose colors to be used in the design.

Requirements
Must have
• derek@brantleystudios.ca
• phone -5873304127
• instagram derek_brantley

```html
<!DOCTYPE html>
<html lang="en">
<head>
<meta charset="utf-8">
<title>Brantley Studios — Business Card</title>
<link rel="stylesheet" href="https://fonts.googleapis.com/css2?family=Roboto:wght@400;500;700&display=swap">
<style>
  :root {
    --page: #e4e4e4;
    --card-white: #ffffff;
    --card-back: #f3f3f3;
    --ink: #1c1c1c;
    --ink-soft: #4a4a4a;
    --grey-text: #8a8a8a;
    --swoosh: #8c8c8c;
    --logo-light: #ffffff;
  }
  * { margin: 0; padding: 0; box-sizing: border-box; }
  html, body {
    width: 1200px; height: 1200px; overflow: hidden;
    background: var(--page);
    font-family: "Roboto", Arial, sans-serif;
  }
  .canvas { position: relative; width: 1200px; height: 1200px; }
  .card {
    position: absolute; left: 262px; width: 686px; height: 392px;
    border-radius: 20px; overflow: hidden;
  }
  .card-front { top: 165px; background: var(--card-white); }
  .card-back { top: 653px; background: var(--card-back); }

  .front-shape { position: absolute; inset: 0; width: 100%; height: 100%; }

  .holder { position: absolute; right: 47px; top: 52px; text-align: right; }
  .holder-name { font-size: 23px; font-weight: 700; color: var(--ink); letter-spacing: 0.2px; }
  .holder-role { font-size: 15px; font-weight: 400; color: var(--grey-text); margin-top: 4px; }

  .contacts { position: absolute; right: 47px; top: 123px; list-style: none; }
  .contact {
    display: flex; align-items: center; justify-content: flex-end; gap: 12px;
    height: 20px; margin-bottom: 10px;
    font-size: 14.5px; color: var(--ink-soft);
  }
  .contact-icon {
    width: 21px; height: 21px; border: 1.5px solid var(--ink);
    border-radius: 50%; display: flex; align-items: center; justify-content: center;
  }
  .contact-icon svg { width: 11px; height: 11px; }

  .front-brand {
    position: absolute; left: 40px; top: 300px;
    font-size: 32px; font-weight: 700; color: var(--logo-light); letter-spacing: 0.5px;
  }
  .tree-art {
    position: absolute; left: 608px; top: 266px; width: 70px; height: 82px;
    background: linear-gradient(180deg, rgba(150,150,150,0.25), rgba(120,120,120,0.8));
    border-radius: 4px;
  }

  .emblem {
    position: absolute; left: 234px; top: 92px; width: 218px; height: 218px;
    border-radius: 50%;
    background: linear-gradient(180deg, #e2e2e2 0%, #9a9a9a 35%, #3a3a3a 60%, #111111 100%);
  }
  .back-brand {
    position: absolute; left: 0; right: 0; top: 226px; text-align: center;
    font-size: 26px; font-weight: 700; color: var(--logo-light);
  }
</style>
</head>
<body>
<main class="canvas">
  <section class="card card-front">
    <svg class="front-shape" viewBox="0 0 800 457" preserveAspectRatio="none" aria-hidden="true">
      <path d="M0,0 L108,0 C140,200 470,340 800,420 L800,457 L0,457 Z" fill="#1c1c1c"/>
      <path d="M118,0 L180,0 C190,170 500,330 800,405 L800,413 C480,338 150,190 118,0 Z" fill="var(--swoosh)"/>
    </svg>

    <div class="holder">
      <p class="holder-name">Derek Brantley</p>
      <p class="holder-role">President</p>
    </div>

    <ul class="contacts">
      <li class="contact">
        <span>5873304127</span>
        <span class="contact-icon">
          <svg viewBox="0 0 24 24"><path fill="#1c1c1c" d="M6.6 10.8a15 15 0 0 0 6.6 6.6l2.2-2.2a1 1 0 0 1 1-.25 11.4 11.4 0 0 0 3.6.57 1 1 0 0 1 1 1V20a1 1 0 0 1-1 1A17 17 0 0 1 3 4a1 1 0 0 1 1-1h3.5a1 1 0 0 1 1 1c0 1.25.2 2.45.57 3.57a1 1 0 0 1-.25 1z"/></svg>
        </span>
      </li>
      <li class="contact">
        <span>derek@brantleystudios.ca</span>
        <span class="contact-icon">
          <svg viewBox="0 0 24 24"><rect x="2" y="5" width="20" height="14" rx="1.5" fill="#1c1c1c"/><path d="M3 6l9 7 9-7" stroke="#fff" stroke-width="1.8" fill="none"/></svg>
        </span>
      </li>
      <li class="contact">
        <span>derek_brantley</span>
        <span class="contact-icon">
          <svg viewBox="0 0 24 24"><circle cx="12" cy="12" r="6" fill="#1c1c1c"/></svg>
        </span>
      </li>
    </ul>

    <p class="front-brand">Brantley Studios</p>
    <div class="tree-art" role="img" aria-label="Small silhouettes of two pine trees"></div>
  </section>

  <section class="card card-back">
    <div class="emblem" role="img" aria-label="Circular monochrome landscape of mountains and pine trees"></div>
    <p class="back-brand">Brantley Studios</p>
  </section>
</main>
</body>
</html>
```